New Advertising Company Business Card

A two sided business card. One side with logo only and the other side with my information and maybe my logo again. Looking for something unique and creative, but not too busy. Info would include my name(Marcus Feldon), President, phone number, address, email address, and website. LOGO IS THE BLUE AND WHITE ONE.

Target Market(s)

CEO/VP Level Audience

Industry/Entity Type

Business

Contact Information for Business Card

In Description.

```html
<!DOCTYPE html>
<html lang="en">
<head>
<meta charset="utf-8">
<title>Lumen Advertising – Business Card</title>
<link rel="stylesheet" href="https://fonts.googleapis.com/css2?family=Montserrat:wght@600;700&family=Open+Sans:wght@400&display=swap">
<style>
  :root {
    --page-bg: #f1f1f1;
    --card-white: #ffffff;
    --card-dark: #232323;
    --brand-blue: #1a74c4;
    --ink: #222222;
    --muted: #555555;
    --rule: #2a2a2a;
  }
  * { box-sizing: border-box; margin: 0; padding: 0; }
  html, body {
    width: 1200px; height: 1200px; overflow: hidden;
    background: var(--page-bg);
    font-family: "Open Sans", sans-serif;
  }
  .card {
    position: absolute;
    left: 170px;
    width: 869px;
    height: 485px;
    border-radius: 26px;
    overflow: hidden;
  }
  .card--front { top: 86px; background: var(--card-white); }
  .card--back { top: 634px; background: var(--card-dark); }

  .wordmark {
    position: absolute;
    font-family: "Montserrat", sans-serif;
    font-weight: 600;
    line-height: 1;
    display: flex;
    align-items: center;
    gap: 14px;
  }
  .wordmark__text { display: flex; flex-direction: column; align-items: flex-end; }
  .wordmark__name { font-size: 60px; letter-spacing: 3px; }
  .wordmark__sub { font-size: 25px; letter-spacing: 6px; margin-top: 8px; }
  .wordmark__dot { width: 22px; height: 22px; border-radius: 50%; background: var(--brand-blue); }

  .card--front .wordmark { right: 43px; top: 108px; color: var(--ink); }
  .card--back .wordmark {
    left: 50%; top: 190px; transform: translateX(-50%);
    color: #ffffff;
  }
  .card--back .wordmark__text { align-items: center; }

  .holder { position: absolute; left: 46px; top: 224px; }
  .holder__name {
    font-family: "Montserrat", sans-serif;
    font-weight: 700; font-size: 31px;
    color: var(--brand-blue);
  }
  .holder__title { font-size: 19px; color: var(--muted); margin-top: 4px; }

  .divider {
    position: absolute; left: 46px; top: 310px;
    width: 780px; height: 2px; background: var(--rule);
  }

  .contacts { position: absolute; left: 46px; top: 326px; list-style: none; }
  .contacts li {
    display: flex; align-items: center; gap: 8px;
    height: 30.5px; font-size: 19.5px; color: var(--muted);
  }
  .contacts svg { width: 20px; height: 20px; fill: var(--brand-blue); }

  .address {
    position: absolute; right: 50px; top: 357px;
    text-align: right; font-size: 19.5px; line-height: 30.5px; color: var(--muted);
    font-style: normal;
  }

  .footer-bands { position: absolute; left: 0; top: 0; width: 869px; height: 485px; }
  .footer-web {
    position: absolute; right: 52px; top: 444px;
    font-size: 19.5px; color: #ffffff;
  }

  .back-web {
    position: absolute; left: 0; right: 0; top: 420px;
    text-align: center; font-size: 19.5px; color: #ffffff; letter-spacing: 0.5px;
  }
  .back-web span { color: var(--brand-blue); }
</style>
</head>
<body>

<section class="card card--front">
  <svg class="footer-bands" viewBox="0 0 869 485" aria-hidden="true">
    <path d="M0 449 H468 C505 449 528 440 566 436 C532 446 506 458 468 458 H0 Z" fill="var(--card-dark)"/>
    <path d="M0 463 H470 C520 463 545 444 600 442 H869 V485 H0 Z" fill="var(--brand-blue)"/>
  </svg>

  <div class="wordmark">
    <div class="wordmark__text">
      <span class="wordmark__name">LUMEN</span>
      <span class="wordmark__sub">ADVERTISING</span>
    </div>
    <span class="wordmark__dot"></span>
  </div>

  <div class="holder">
    <h1 class="holder__name">Marcus Feldon</h1>
    <p class="holder__title">President</p>
  </div>

  <div class="divider"></div>

  <ul class="contacts">
    <li>
      <svg viewBox="0 0 24 24" aria-label="Phone"><path d="M6.6 10.8a15.1 15.1 0 0 0 6.6 6.6l2.2-2.2c.3-.3.7-.4 1-.2 1.1.4 2.3.6 3.6.6.6 0 1 .4 1 1V20c0 .6-.4 1-1 1A17 17 0 0 1 3 4c0-.6.4-1 1-1h3.5c.6 0 1 .4 1 1 0 1.3.2 2.5.6 3.6.1.3 0 .7-.2 1z"/></svg>
      +000.000.00 00
    </li>
    <li>
      <svg viewBox="0 0 24 24" aria-label="Mobile"><path d="M7 1h10a2 2 0 0 1 2 2v18a2 2 0 0 1-2 2H7a2 2 0 0 1-2-2V3a2 2 0 0 1 2-2zm0 3v14h10V4zm5 15.5a1.2 1.2 0 1 0 0 2.4 1.2 1.2 0 0 0 0-2.4z"/></svg>
      +000.000.00 00
    </li>
    <li>
      <svg viewBox="0 0 24 24" aria-label="Email"><path d="M2 5h20v14H2zm2 2v.4l8 5.2 8-5.2V7zm0 2.8V17h16V9.8l-8 5.2z"/></svg>
      info@lumenadvertising.com
    </li>
  </ul>

  <address class="address">
    Street Name Avenue, Suite<br>
    100 State, Zip Code,Country
  </address>

  <p class="footer-web">www.lumenadvertising.com</p>
</section>

<section class="card card--back">
  <div class="wordmark">
    <div class="wordmark__text">
      <span class="wordmark__name">LUMEN</span>
      <span class="wordmark__sub">ADVERTISING</span>
    </div>
    <span class="wordmark__dot"></span>
  </div>
  <p class="back-web"><span>www.</span>lumenadvertising<span>.com</span></p>
</section>

</body>
</html>
```